2 Funky Pages + EASY stock logo = Construction Website

We would like a funky new website - Just 2 pages - to promote our project management company. A logo is also needed, but we'll provide a stock image which just needs a colour change a text added.

Here are the instructions:

"Fair Tally Homes"

#logo
The one I'd like is attached. Please change font and positioning of text though.

Tagline is "Don't be normal - Be clever"

#Colour combo
756897 Wood Veneer
D5D6D2 sand dollar
353C3F charcoal
962715 brick red

#Home - Page 1

Our cost-price home build service will save you thousands.
No, seriously - Here's how we do it (button)

- Pay what the home building companies do.
- FTH will manage the entire project.
- Use Keystonecraft Guaranteed builders and materials.
- Tender for the best industry rates.
- Get a full budget calculated for the build.
- Avoid inflated 'Fixed-price' builds.
See how it works (button)

Contact Us: 0800 615 278
enquire - Name, Phone, email, comment - SEND

#How it works - Page 2

Traditional fixed price contracts are popular because it means that any risk of unexpected problems is carried by the home builder, but the builder will generally load the price about 10 times above the actual risk carried.

It's like an over-priced insurance policy, on steroids.

Clever people do things differently.

Here's how a cost-price build works...

1) Tell us what you want to build. Dream home, townhouse, investment property, whatever.

2) We'll put a design together for you, or you can choose from a bunch of plans we've already got.

3) We'll give you a conservative price estimate.

4) We finish tweaking your plans, then send them out to our network of more than 200 builders, subcontractors and tradesmen.

5) We collect the quotes, pick the best prices, and finalise your budget. Now you buy us beer, cause you've finally realised how much you're saving.

6) Tell your friends how awesome we are, while we lodge your building consent application with Council.

7) We coordinate the builders and subbies (look, you're already speaking trade-talk) from start to finish. You pay the cost price on their work each month.

We're happy to talk numbers and give you an estimate.

Contact Us: 0800 615 278

Reason: I have seen some great design elements, but need them to come together in one site design. Also, there appears to be less attention paid to the second page design ('how it works') than is necessary... There is no viable contender there yet, compared with the great home page submissions. I've also added some further info to the brief, and note that many submissions have ignored the colour combo I've requested.

Industry/Entity Type

Construction

Number of Pages Required

2 page

Requirements
Must have
• Keystonecrafter logo (small)
• Colour combo described in brief.
Nice to have
• I've attached a stock image I like, but it's certainly not essential. I do like images with clear backgrounds though - they tend to produce a crisp looking site.
• There is a wider image similar to this, available on Pixel Vault, but Sketch Hive won't let me attach it.
Should not have
• Photos of cheesy American faces.

```html
<!DOCTYPE html>
<html lang="en">
<head>
<meta charset="utf-8">
<title>Fair Tally Homes — Construction</title>
<link rel="stylesheet" href="https://fonts.googleapis.com/css2?family=Raleway:wght@400;500;600&family=Roboto:wght@300;400;500;700&display=swap">
<style>
  :root {
    --charcoal: #353c3f;
    --ink: #141414;
    --brick: #962715;
    --brick-light: #a52d1c;
    --sand: #d5d6d2;
    --veneer: #756897;
    --lime: #b6d332;
    --paper: #f4f4f4;
    --text: #555;
    --heading: #4a4a4a;
    --white: #fff;
  }
  * { box-sizing: border-box; margin: 0; padding: 0; }
  html, body { width: 803px; height: 1200px; overflow: hidden; background: var(--white); }
  body { position: relative; font-family: 'Roboto', Arial, sans-serif; color: var(--text); }
  .abs { position: absolute; }

  /* Hero */
  .hero-photo { left: 0; top: 0; width: 803px; height: 325px;
    background: linear-gradient(180deg, #4e5a66 0%, #2c2a2a 35%, #2a1b14 70%, #1a120e 100%); }
  .brand { left: 66px; top: 18px; display: flex; align-items: center; gap: 6px; }
  .brand-mark { width: 14px; height: 14px; background: var(--lime); }
  .brand-name { font-family: 'Roboto', sans-serif; font-size: 10px; font-weight: 500; color: var(--lime); }
  .topbar { top: 21px; font-size: 8px; color: var(--white); }
  .topbar.news { left: 409px; font-weight: 300; }
  .topbar.sep { left: 492px; opacity: .7; }
  .topbar.quick { left: 506px; font-size: 9px; font-weight: 500; top: 20px; }
  .social { top: 22px; width: 7px; height: 7px; border-radius: 50%; background: var(--white); }
  .nav { top: 45px; font-size: 9px; color: var(--white); }
  .nav.active { color: var(--lime); }
  .tagline-frame { left: 146px; top: 118px; width: 512px; height: 82px; border: 1px solid rgba(255,255,255,.55); }
  .tagline-inner { left: 150px; top: 122px; width: 504px; height: 74px; border: 1px solid rgba(255,255,255,.35);
    display: flex; align-items: center; justify-content: center; }
  .tagline { font-family: 'Roboto', sans-serif; font-weight: 500; font-size: 28px; color: var(--white); letter-spacing: .3px; }
  .slide-arrow { top: 150px; }

  /* How it works */
  .works-band { left: 0; top: 270px; width: 803px; height: 170px; }
  .section-title { width: 803px; left: 0; text-align: center; font-family: 'Raleway', sans-serif; font-weight: 500; color: var(--heading); }
  .works-title { top: 328px; font-size: 20px; }
  .works-copy { left: 200px; top: 362px; width: 403px; text-align: center; font-size: 8px; line-height: 13.7px; color: #555; }

  .steps-title { top: 482px; font-size: 20px; }
  .steps-sub { top: 513px; font-size: 11.5px; font-family: 'Raleway', sans-serif; color: #555; font-weight: 400; }
  .steps { left: 66px; top: 553px; width: 260px; list-style: none; }
  .steps li { position: relative; padding-left: 21px; font-size: 9px; line-height: 14px; color: #666; font-weight: 300; margin-bottom: 9.6px; }
  .steps li svg { position: absolute; left: 0; top: 3px; }

  .video-frame { left: 353px; top: 557px; width: 385px; height: 234px; background: var(--white);
    box-shadow: 0 0 3px rgba(0,0,0,.35); }
  .video-still { left: 5px; top: 5px; width: 375px; height: 224px;
    background: linear-gradient(160deg, #b9cde0 0%, #dfe6ec 35%, #9ea4a8 60%, #c7c9c8 100%); }
  .video-play { left: 169px; top: 94px; }

  /* Contact band */
  .site-photo { left: 0; top: 847px; width: 400px; height: 270px;
    background: linear-gradient(180deg, #6b4a28 0%, #8a5a2a 35%, #4a2d18 70%, #1e1510 100%); }
  .band-title { left: 0; width: 468px; text-align: center; color: var(--white); font-family: 'Raleway', sans-serif; }
  .band-title.main { top: 924px; font-size: 21px; font-weight: 500; }
  .band-title.sub { top: 951px; font-size: 14.5px; font-weight: 400; }
  .call-button { left: 132px; top: 993px; width: 204px; height: 33px; background: var(--brick-light);
    color: var(--white); font-size: 14.5px; display: flex; align-items: center; justify-content: center; }

  .enquire-title { left: 400px; width: 336px; top: 890px; text-align: center; color: var(--white);
    font-family: 'Raleway', sans-serif; font-weight: 500; font-size: 18px; }
  .field { height: 28px; background: rgba(255,255,255,.16); color: var(--white); font-size: 7.5px;
    padding-left: 12px; display: flex; align-items: center; }
  .hint { left: 426px; top: 1040px; font-size: 9px; color: var(--white); font-weight: 300; }
  .send { left: 623px; top: 1032px; width: 85px; height: 29px; border: 1px solid var(--white); color: var(--white);
    font-size: 10.5px; display: flex; align-items: center; justify-content: center; }

  .badge { left: 66px; top: 1117px; width: 52px; height: 62px; background: #1d4e8f; }
  .copyright { right: 66px; top: 1157px; font-size: 8px; color: #777; }
</style>
</head>
<body>

  <!-- Hero -->
  <div class="abs hero-photo" role="img" aria-label="Silhouetted workers on a building site with concrete pump boom at dusk"></div>
  <div class="abs brand"><span class="brand-mark"></span><span class="brand-name">Fair Tally Homes</span></div>
  <span class="abs topbar news">SIGN UP FOR NEWS</span>
  <span class="abs topbar sep">|</span>
  <span class="abs topbar quick">Quick contact - (612) 470-3925</span>
  <span class="abs social" style="left:656px"></span>
  <span class="abs social" style="left:673px"></span>
  <span class="abs social" style="left:692px"></span>
  <span class="abs social" style="left:711px"></span>
  <span class="abs social" style="left:730px;background:var(--lime)"></span>

  <span class="abs nav active" style="left:327px">Home</span>
  <span class="abs nav" style="left:388px">About us</span>
  <span class="abs nav" style="left:462px">Blog</span>
  <span class="abs nav" style="left:517px">Gallery</span>
  <span class="abs nav" style="left:582px">News</span>
  <span class="abs nav" style="left:641px">Bio</span>
  <span class="abs nav" style="left:691px">Contact us</span>

  <div class="abs tagline-frame"></div>
  <div class="abs tagline-inner"><h1 class="tagline">DON'T BE NORMAL - BE CLEVER</h1></div>

  <svg class="abs slide-arrow" style="left:23px" width="28" height="28" viewBox="0 0 28 28"><circle cx="14" cy="14" r="13" fill="none" stroke="rgba(255,255,255,.5)" stroke-width="1.3"/><path d="M16 8l-6 6 6 6" fill="none" stroke="rgba(255,255,255,.6)" stroke-width="1.5"/></svg>
  <svg class="abs slide-arrow" style="left:755px" width="28" height="28" viewBox="0 0 28 28"><circle cx="14" cy="14" r="13" fill="none" stroke="rgba(255,255,255,.5)" stroke-width="1.3"/><path d="M12 8l6 6-6 6" fill="none" stroke="rgba(255,255,255,.6)" stroke-width="1.5"/></svg>

  <!-- How it works band -->
  <svg class="abs works-band" width="803" height="170" viewBox="0 0 803 170">
    <defs><linearGradient id="bandShadow" x1="0" y1="0" x2="0" y2="1"><stop offset="0" stop-color="#000" stop-opacity=".08"/><stop offset="1" stop-color="#000" stop-opacity="0"/></linearGradient></defs>
    <polygon points="0,55 50,55 398,4 750,55 803,55 803,167 0,167" fill="var(--paper)"/>
    <polygon points="398,4 750,55 803,55 803,120 560,167 330,167" fill="#efefef"/>
    <polygon points="0,55 50,55 260,110 80,167 0,167" fill="#f0f0f0"/>
    <rect x="0" y="167" width="803" height="3" fill="url(#bandShadow)"/>
  </svg>

  <h2 class="abs section-title works-title">How it works</h2>
  <p class="abs works-copy">Traditional fixed price contracts are popular because it means that any risk of unexpected problems is carried by the home builder, but the builder will generally load the price about 10 times above the actual risk carried. It's like an over-priced insurance policy, on steroids. Clever people do things differently.</p>

  <h2 class="abs section-title steps-title">Here's how a cost-price build works...</h2>
  <p class="abs section-title steps-sub">We're happy to talk numbers and give you an estimate</p>

  <ul class="abs steps">
    <li><svg width="9" height="8" viewBox="0 0 9 8"><path d="M1 4l2.5 2.5L8 1" fill="none" stroke="#555" stroke-width="1.6"/></svg>Tell us what you want to build. Dream home, townhouse, investment property, whatever.</li>
    <li><svg width="9" height="8" viewBox="0 0 9 8"><path d="M1 4l2.5 2.5L8 1" fill="none" stroke="#555" stroke-width="1.6"/></svg>We'll put a design together for you, or you can choose from a bunch of plans we've already got.</li>
    <li><svg width="9" height="8" viewBox="0 0 9 8"><path d="M1 4l2.5 2.5L8 1" fill="none" stroke="#555" stroke-width="1.6"/></svg>We'll give you a conservative price estimate.</li>
    <li><svg width="9" height="8" viewBox="0 0 9 8"><path d="M1 4l2.5 2.5L8 1" fill="none" stroke="#555" stroke-width="1.6"/></svg>We finish tweaking your plans, then send them out to our network of more than 200 builders, subcontractors</li>
    <li><svg width="9" height="8" viewBox="0 0 9 8"><path d="M1 4l2.5 2.5L8 1" fill="none" stroke="#555" stroke-width="1.6"/></svg>We collect the quotes, pick the best prices, and finalise your budget. Now you buy us beer, cause you've</li>
    <li><svg width="9" height="8" viewBox="0 0 9 8"><path d="M1 4l2.5 2.5L8 1" fill="none" stroke="#555" stroke-width="1.6"/></svg>Tell your friends how awesome we are, while we lodge your building consent application with Council.</li>
    <li><svg width="9" height="8" viewBox="0 0 9 8"><path d="M1 4l2.5 2.5L8 1" fill="none" stroke="#555" stroke-width="1.6"/></svg>We coordinate the builders and subbies (look, you're already speaking trade-talk) from start to finish.</li>
  </ul>

  <div class="abs video-frame">
    <div class="abs video-still" role="img" aria-label="Video still: worker in red overalls setting a precast concrete slab on a high-rise site under a blue sky"></div>
    <svg class="abs video-play" width="38" height="38" viewBox="0 0 38 38"><circle cx="19" cy="19" r="17" fill="rgba(0,0,0,.15)" stroke="#fff" stroke-width="2"/><path d="M15 12l11 7-11 7z" fill="none" stroke="#fff" stroke-width="1.8" stroke-linejoin="round"/></svg>
  </div>

  <!-- Contact band -->
  <div class="abs site-photo" role="img" aria-label="Cranes and workers on a construction site at golden sunset"></div>
  <svg class="abs" style="left:0;top:847px" width="803" height="353" viewBox="0 0 803 353">
    <polygon points="400,0 803,0 803,243 400,293" fill="var(--brick)"/>
    <polygon points="560,0 803,0 803,120 620,200" fill="#9c2b18" opacity=".6"/>
    <polygon points="0,270 400,243 400,293 803,243 803,353 0,353" fill="var(--ink)"/>
  </svg>

  <h3 class="abs band-title main">We Are Fair Tally Homes</h3>
  <p class="abs band-title sub">Construction Company</p>
  <div class="abs call-button">Contact Us: 0800 615 278</div>

  <h3 class="abs enquire-title">Enquire</h3>
  <div class="abs field" style="left:429px;top:926px;width:135px">Name *</div>
  <div class="abs field" style="left:573px;top:926px;width:135px">Phone Number *</div>
  <div class="abs field" style="left:429px;top:962px;width:279px">Mail id *</div>
  <div class="abs field" style="left:429px;top:997px;width:279px">Commends *</div>
  <span class="abs hint">Click Here To send your enquire questions *</span>
  <div class="abs send">Send Now</div>

  <div class="abs badge" aria-label="Keystonecrafter registration badge"></div>
  <span class="abs copyright">Copyrights@2016 Company Name , all rights reserved</span>

</body>
</html>
```